Wholesale Catalogue Design for Greeting Cards

Wren Ink is a small letterpress printery, I would like to have a wholesale catalogue designed for my range of letterpress greeting cards. I currently have 30 cards in my collection, I can supply photos, I want to be able to add to the catalogue in the future. I also want the design to represent my card designs: fun, colourful and with an elegant edge, featuring a mix of my original illustrations and hand lettering along with downloadable designs and fonts.
I would like to be able to email the catalogue to my wholesale customers and to be able to print the catalogue to use with new/potential wholesale customers.

Target Market(s)

Small boutique retailers, gift shops, baby/kids gift shops, florists

Industry/Entity Type

Wholesale

Font styles to use
Serif

Colors
eea4c8

Requirements
Must have
• I have been using baskerville font in my branding, so it would be good to include this in the design. I can provide photos and text. I also have a pink and black logo (seen attached), it would be great if the design can incorporate some of the same colour scheme.
Nice to have
• I have added some pics below of other catalogues I like the layout of.
• You can also view my work at craftlane.com/wrenink or wreninkdesign.com
• * I believe I have now loaded all the relevant photos and info
• ** I have uploaded some pics of my attempt at a wholesale catalogue and my current order sheet as this outlines the products I want in the catalogue and the different card sections. my catalogue attempt has more recent photos. I will upload photos of the remaining products by end of today (27.2.16)

```html
<!DOCTYPE html>
<html lang="en">
<head>
<meta charset="utf-8">
<title>Wren Ink – Wholesale Order Form &amp; Terms</title>
<link rel="stylesheet" href="https://fonts.googleapis.com/css2?family=Libre+Baskerville&family=Source+Sans+3:wght@400;600;700&display=swap">
<style>
  :root {
    --pink: #eba5a8;
    --pink-soft: #f2c7c9;
    --pink-line: #e9a3a6;
    --pink-faint: #f6dcdd;
    --ink: #1e1e1e;
    --grey-line: #c9c9c9;
    --alert: #e2332f;
    --paper: #ffffff;
  }
  html, body { margin: 0; padding: 0; overflow: hidden; background: var(--paper); }
  .spread {
    position: relative; width: 1200px; height: 424px; overflow: hidden;
    background: var(--paper); color: var(--ink);
    font-family: "Source Sans 3", Arial, sans-serif;
  }
  .page-title {
    position: absolute; top: 34px; margin: 0;
    font-family: "Libre Baskerville", Georgia, serif; font-weight: 400;
    font-size: 17px; letter-spacing: 1.2px; color: var(--pink);
  }
  .page-title--order { left: 26px; }
  .page-title--terms { left: 626px; }

  .sender {
    position: absolute; left: 26px; top: 69px; margin: 0;
    font-size: 8.4px; line-height: 10.5px; font-style: normal;
  }

  .fields { position: absolute; top: 68px; height: 64px; }
  .fields--billing { left: 134px; width: 214px; }
  .fields--shipping { left: 358px; width: 216px; }
  .fields__tab {
    position: absolute; left: 0; top: 0; width: 10px; height: 64px;
    background: var(--pink-soft);
  }
  .fields__tab span {
    position: absolute; left: 50%; top: 50%;
    transform: translate(-50%, -50%) rotate(-90deg);
    color: #fff; font-size: 6.5px; font-weight: 700; letter-spacing: 0.8px;
  }
  .fields__rows { position: absolute; left: 14px; right: 0; top: 10px; }
  .field-row {
    position: relative; height: 14.5px; border-top: 0.6px solid var(--grey-line);
    font-size: 5.4px;
  }
  .field-row span { position: absolute; top: 2px; }

  .order-table {
    position: absolute; top: 148px; border-collapse: collapse;
    table-layout: fixed; font-size: 8px;
    border: 0.8px solid var(--pink-line);
  }
  .order-table--left { left: 26px; width: 272px; }
  .order-table--right { left: 306px; width: 268px; }
  .order-table th {
    background: var(--pink-soft); font-weight: 400; font-size: 9.5px;
    height: 20px; line-height: 20px; text-align: left; padding: 0 0 0 6px;
    border-left: 0.8px solid var(--pink-line); box-sizing: border-box;
  }
  .order-table tbody tr { height: 10px; }
  .order-table td {
    height: 9.5px; padding: 0 0 0 6px; line-height: 9.5px;
    border-left: 0.8px solid var(--pink-line);
    border-top: 0.5px solid var(--pink-faint);
    white-space: nowrap; overflow: hidden;
  }
  .order-table .section td:nth-child(2) { font-weight: 700; }
  .order-table th:first-child, .order-table td:first-child { border-left: none; }
  .order-table sup { font-size: 5px; line-height: 0; vertical-align: 3px; }
  .header-tick {
    position: absolute; left: 525px; top: 128px; width: 0.8px; height: 20px;
    background: var(--pink-line);
  }

  .terms {
    position: absolute; top: 69px; font-size: 6.75px; line-height: 8.8px;
  }
  .terms--intro { left: 626px; width: 262px; }
  .terms--policy { left: 904px; width: 268px; }
  .terms p { margin: 0; }
  .terms h3 {
    margin: 0; font-size: 6.75px; font-weight: 600; color: var(--pink);
    text-transform: uppercase; letter-spacing: 0.2px;
  }
  .terms .gap { margin-top: 8.8px; }
  .terms .alert { color: var(--alert); }
  .terms strong { font-weight: 700; }
  .terms a { color: inherit; text-decoration: underline; }
  .terms .sign-off { margin-top: 26px; }
</style>
</head>
<body>
<main class="spread">

  <h1 class="page-title page-title--order">ORDER FORM</h1>

  <address class="sender">
    Wren Ink Design<br>
    24 Linden Cres.<br>
    Port Willow, WA&nbsp; 6172<br>
    Tel: +61(0) 400218675<br>
    www.wrenink.com.au<br>
    hattie@wreninkdesign.com
  </address>

  <section class="fields fields--billing" aria-label="Billing details">
    <div class="fields__tab"><span>BILLING</span></div>
    <div class="fields__rows">
      <div class="field-row"><span style="left:6px">Name</span><span style="left:186px">Date</span></div>
      <div class="field-row"><span style="left:6px">Address</span></div>
      <div class="field-row"><span style="left:6px">City</span><span style="left:110px">State</span><span style="left:186px">Zip</span></div>
      <div class="field-row"><span style="left:0">Country</span><span style="left:68px">Phone</span><span style="left:134px">Email</span></div>
    </div>
  </section>

  <section class="fields fields--shipping" aria-label="Shipping details">
    <div class="fields__tab"><span>SHIPPING</span></div>
    <div class="fields__rows">
      <div class="field-row"><span style="left:6px">Name</span><span style="left:190px">Date</span></div>
      <div class="field-row"><span style="left:6px">Address</span></div>
      <div class="field-row"><span style="left:6px">City</span><span style="left:110px">State</span><span style="left:190px">Zip</span></div>
      <div class="field-row"><span style="left:0">Country</span><span style="left:68px">Phone</span><span style="left:136px">Email</span></div>
    </div>
  </section>

  <div class="header-tick"></div>

  <table class="order-table order-table--left">
    <colgroup><col style="width:31px"><col style="width:120px"><col style="width:36px"><col style="width:32px"><col style="width:53px"></colgroup>
    <thead><tr><th>SKU</th><th>DESCRIPTION</th><th>PRICE</th><th>QTY</th><th>TOTAL</th></tr></thead>
    <tbody>
      <tr><td></td><td></td><td></td><td></td><td></td></tr>
      <tr class="section"><td></td><td>NEW BABY</td><td></td><td></td><td></td></tr>
      <tr><td>A001</td><td>Double Dots</td><td>3.55</td><td></td><td></td></tr>
      <tr><td>A002</td><td>Little Sprout</td><td>3.55</td><td></td><td></td></tr>
      <tr><td>A003</td><td>Hello Tiny - pink</td><td>3.55</td><td></td><td></td></tr>
      <tr><td>A004</td><td>Hello Tiny - blue</td><td>3.55</td><td></td><td></td></tr>
      <tr><td>A005</td><td>Baby Bloom - pink</td><td>3.55</td><td></td><td></td></tr>
      <tr><td>A006</td><td>Baby Bloom - lilac</td><td>3.55</td><td></td><td></td></tr>
      <tr class="section"><td></td><td>KIDS BIRTHDAY</td><td></td><td></td><td></td></tr>
      <tr><td>B001</td><td>1<sup>st</sup> Birthday Bloom</td><td>3.55</td><td></td><td></td></tr>
      <tr><td>B002</td><td>2<sup>nd</sup> Birthday Bloom</td><td>3.55</td><td></td><td></td></tr>
      <tr><td>B003</td><td>3<sup>rd</sup> Birthday</td><td>3.55</td><td></td><td></td></tr>
      <tr><td>B004</td><td>Hopping Hare</td><td>3.55</td><td></td><td></td></tr>
      <tr class="section"><td></td><td>BIRTHDAY CARDS</td><td></td><td></td><td></td></tr>
      <tr><td>C001</td><td>Happy Birthday - pink stars</td><td>3.55</td><td></td><td></td></tr>
      <tr><td>C002</td><td>Happy Birthday - green stars</td><td>3.55</td><td></td><td></td></tr>
      <tr><td>C003</td><td>Big Top</td><td>3.55</td><td></td><td></td></tr>
      <tr><td>C004</td><td>Happy Birthday Bloom</td><td>3.55</td><td></td><td></td></tr>
      <tr class="section"><td></td><td>FATHER'S DAY</td><td></td><td></td><td></td></tr>
      <tr><td>I001</td><td>Top Pop</td><td>3.55</td><td></td><td></td></tr>
      <tr><td>I002</td><td>Happy Father's Day (end of Feb)</td><td>3.55</td><td></td><td></td></tr>
      <tr><td></td><td></td><td></td><td></td><td></td></tr>
      <tr><td></td><td></td><td></td><td></td><td></td></tr>
    </tbody>
  </table>

  <table class="order-table order-table--right">
    <colgroup><col style="width:31px"><col style="width:120px"><col style="width:36px"><col style="width:32px"><col style="width:49px"></colgroup>
    <thead><tr><th>SKU</th><th>DESCRIPTION</th><th>PRICE</th><th>QTY</th><th>TOTAL</th></tr></thead>
    <tbody>
      <tr><td></td><td></td><td></td><td></td><td></td></tr>
      <tr class="section"><td></td><td>WEDDING • ENGAGEMENT</td><td></td><td></td><td></td></tr>
      <tr><td>D001</td><td>Mr. &amp; Mrs.</td><td>3.55</td><td></td><td></td></tr>
      <tr><td>D002</td><td>Mr. &amp; Mr.</td><td>3.55</td><td></td><td></td></tr>
      <tr><td>D003</td><td>Just Wed</td><td>3.55</td><td></td><td></td></tr>
      <tr><td>D004</td><td>Two Hearts</td><td>3.55</td><td></td><td></td></tr>
      <tr class="section"><td></td><td>LOVE • VALENTINE'S DAY</td><td></td><td></td><td></td></tr>
      <tr><td>E001</td><td>Sweet Pea</td><td>3.55</td><td></td><td></td></tr>
      <tr><td>E002</td><td>Nuts For You</td><td>3.55</td><td></td><td></td></tr>
      <tr><td>E003</td><td>I Love You - pink</td><td>3.55</td><td></td><td></td></tr>
      <tr><td>E004</td><td>I Love You - black</td><td>3.55</td><td></td><td></td></tr>
      <tr class="section"><td></td><td>GENERAL</td><td></td><td></td><td></td></tr>
      <tr><td>F001</td><td>Country Lane</td><td>3.55</td><td></td><td></td></tr>
      <tr><td>F002</td><td>Congratulations (end of Feb)</td><td>3.55</td><td></td><td></td></tr>
      <tr><td>F003</td><td>Sympathy (end of Feb)</td><td>3.55</td><td></td><td></td></tr>
      <tr class="section"><td></td><td>MOTHER'S DAY</td><td></td><td></td><td></td></tr>
      <tr><td>G001</td><td>Lovely Mum - purple</td><td>3.55</td><td></td><td></td></tr>
      <tr><td>G002</td><td>Best Mum</td><td>3.55</td><td></td><td></td></tr>
      <tr><td>G003</td><td>Happy Mother's Day - flower</td><td>3.55</td><td></td><td></td></tr>
      <tr><td></td><td></td><td></td><td></td><td></td></tr>
      <tr><td></td><td></td><td></td><td></td><td></td></tr>
      <tr><td></td><td></td><td></td><td></td><td></td></tr>
      <tr><td></td><td></td><td></td><td></td><td></td></tr>
    </tbody>
  </table>

  <h2 class="page-title page-title--terms">TERMS &amp; CONDITIONS</h2>

  <section class="terms terms--intro">
    <p>Welcome to Wren Ink Wholesale, I trust this is the beginning of a beautiful friendship. Remember you can contact me anytime at:<br>
    <strong>hattie@wreninkdesign.com</strong> or <strong>+61(0)400218675</strong></p>

    <h3 class="gap">Step 1</h3>
    <p>Get a cup of tea or coffee and find a comfy spot to browse the Wren Ink Catalogue (or check out my Craftlane shop <a>craftlane.com/wrenink</a> )</p>
    <h3>Step 2</h3>
    <p>Spend as much time as you like perusing my catalogue and choosing the right beautiful, original letterpress stationery for you.</p>
    <h3>Step 3</h3>
    <p>&nbsp;Time to order, fill out my basic order form and email said form back to me. I will be in contact within 48hours with confirmation of your order and approximate delivery times.</p>
    <h3>Step 4</h3>
    <p>Get excited like a kid at Christmas time while you wait for your order to arrive!</p>

    <h3 class="gap">Please note</h3>
    <p>• All Wren Ink stationery is hand printed on a 120 year old press some irregularities in the prints may occur, I prefer to look at this as a beauty mark, making each card and print truly unique. Please contact me if you have a colour request in mind for your order and I will do my best to accommodate. (please note this may create additional production time and possible delay of order).</p>
    <p>• If you have any questions, requests, great feedback or just a great recipe for flourless chocolate cake please don't hesitate to contact me.</p>
  </section>

  <section class="terms terms--policy">
    <h3>Minimum order value</h3>
    <p>• Minimum opening order value of $80.00 plus postage ($8-15 within Australia) is required; orders thereafter are $50.00 plus postage.</p>
    <h3>Lead time</h3>
    <p>• I keep stock on hand and ready for sale, in most cases I can fill an order immediately. If an item is out of stock lead time will be 5-10 business days.</p>
    <h3>Deliveries</h3>
    <p>• Please check order form to ensure products you order are in stock (out of stock products will be listed as 'out of stock'). If you wish to order an out of stock item, don't worry I can help, send me an email and I will let you know how long it will take for me to fill your order, easy!</p>
    <p>• Postage will be calculated on an order basis, depending on weight and will be sent registered post unless you would prefer otherwise.</p>
    <p>• All stationery is sized to fit into an A4 postage package and will arrive professionally packaged with a stiff card backing, in a clear plastic sleeve and wrapped in bubble wrap for extra protection.</p>
    <h3>Payments</h3>
    <p>• All payments are to be made by <span class="alert">EFT (electronic funds transfer)</span> to me, Hattie Marsh BSB 000 118 A/C 224 306 with your retail name as reference and cleared prior to despatch. I can also invoice via PayLink.</p>
    <h3>Cancelled/unpaid orders</h3>
    <p>• Any customer payment request for orders that remain unpaid in excess of 20 days will be unpacked and the order cancelled.</p>
    <h3>Returns</h3>
    <p>While I do not offer refunds on unsold products, I am happy to exchange unsold/ undamaged product within 30 days of purchase for new stock.</p>

    <p class="sign-off">Regards,<br><strong>Hattie Marsh</strong><br><strong>Wren Ink</strong></p>
  </section>

</main>
</body>
</html>
```